Telecommunications/Power civil contractor needs business card design

Were a new telecommunications/power underground civil contractor that is looking for a new business card design. Our company colours are silver or grey and orange. Feel free to use the white background logo or the black background logo.

Target Market(s)

Local contractors, utility companies, private sector mining/energy companies, developers.

Industry/Entity Type

Telecommunications

Contact Information for Business Card

Each card will need the following info:
Persons name:
Title:
E-mail:
Phone number:
Shop Address:
Mailing Address:

Requirements
Must have
• Each card will need the following info:
• Persons name:
• Title:
• E-mail:
• Phone number:
• Shop Address:
• Mailing Address:

```html
<!DOCTYPE html>
<html lang="en">
<head>
<meta charset="utf-8">
<title>Holt Line Civil Inc – Business Card</title>
<link rel="stylesheet" href="https://fonts.googleapis.com/css2?family=Lato:wght@400;700;900&display=swap">
<style>
  :root {
    --backdrop: #2a2a2a;
    --card: #f7f7f7;
    --orange: #e0531d;
    --grey-dark: #4a4a4a;
    --grey-text: #555555;
    --grey-band: #5a5a5a;
  }
  * { box-sizing: border-box; margin: 0; padding: 0; }
  html, body {
    width: 1200px; height: 873px; overflow: hidden;
    background: var(--backdrop);
    font-family: "Lato", sans-serif;
  }
  .card {
    position: absolute; left: 170px; top: 191px;
    width: 860px; height: 490px;
    background: var(--card);
    overflow: hidden;
  }
  .holder { position: absolute; left: 56px; top: 70px; }
  .holder-name { color: var(--orange); font-weight: 700; font-size: 26px; }
  .holder-title { color: var(--grey-text); font-size: 19px; margin-top: 2px; }

  .brand {
    position: absolute; right: 64px; top: 56px;
    display: flex; flex-direction: column; align-items: center; gap: 12px;
  }
  .brand-dot {
    width: 74px; height: 74px; border-radius: 50%;
    border: 6px solid var(--orange);
  }
  .brand-name {
    color: var(--orange); font-weight: 900; font-size: 26px;
    letter-spacing: 1px; text-transform: uppercase;
  }

  .contacts {
    position: absolute; left: 56px; bottom: 84px;
    list-style: none; display: flex; flex-direction: column; gap: 10px;
  }
  .contact { display: flex; align-items: center; gap: 14px; color: var(--grey-dark); font-size: 19px; }
  .contact svg { width: 18px; height: 18px; fill: var(--orange); flex: none; }
  .contact-label { color: var(--orange); font-size: 16px; margin-left: 8px; }

  .bands { position: absolute; left: 0; bottom: 0; width: 860px; height: 64px; }
  .band-orange { fill: var(--orange); }
  .band-grey { fill: var(--grey-band); }
</style>
</head>
<body>
  <main class="card">
    <header class="holder">
      <h1 class="holder-name">Daniel Korvek</h1>
      <p class="holder-title">Chief Operating Officer</p>
    </header>

    <div class="brand">
      <span class="brand-dot"></span>
      <span class="brand-name">Holt Line Civil Inc</span>
    </div>

    <ul class="contacts">
      <li class="contact">
        <svg viewBox="0 0 24 24"><path d="M6.6 10.8a15.1 15.1 0 0 0 6.6 6.6l2.2-2.2a1 1 0 0 1 1-.25 11.4 11.4 0 0 0 3.6.57 1 1 0 0 1 1 1V20a1 1 0 0 1-1 1A17 17 0 0 1 3 4a1 1 0 0 1 1-1h3.5a1 1 0 0 1 1 1c0 1.25.2 2.45.57 3.57a1 1 0 0 1-.25 1z"/></svg>
        412-555-0148
      </li>
      <li class="contact">
        <svg viewBox="0 0 24 24"><path d="M2 5h20v14H2z M3 6l9 7 9-7" stroke="#f7f7f7" stroke-width="1.5"/></svg>
        enquiries@holtlinecivil.com
      </li>
      <li class="contact">
        <svg viewBox="0 0 24 24"><path d="M12 2a7 7 0 0 0-7 7c0 5.2 7 13 7 13s7-7.8 7-13a7 7 0 0 0-7-7zm0 9.5A2.5 2.5 0 1 1 12 6.5a2.5 2.5 0 0 1 0 5z"/></svg>
        42 Alder Lane, Fairbrook, PA 15090<span class="contact-label">(Shop Address)</span>
      </li>
      <li class="contact">
        <svg viewBox="0 0 24 24"><path d="M12 2a7 7 0 0 0-7 7c0 5.2 7 13 7 13s7-7.8 7-13a7 7 0 0 0-7-7zm0 9.5A2.5 2.5 0 1 1 12 6.5a2.5 2.5 0 0 1 0 5z"/></svg>
        #1180 Cedar Street, Lakemont, New York<span class="contact-label">(Mailing Address)</span>
      </li>
    </ul>

    <svg class="bands" viewBox="0 0 860 64" preserveAspectRatio="none">
      <rect class="band-orange" x="0" y="44" width="600" height="20"/>
      <path class="band-grey" d="M560 64 C585 64 590 16 630 16 L860 16 L860 64 Z"/>
    </svg>
  </main>
</body>
</html>
```